Boundless Haulbins Billboard design

I need two billboard designs using our logo and adding a few words Looking for a black background with our logo and wording in either purple or white.

need it to have our website boundlesshaulbins.com. phone number 555 314 2087

Also have 16/20/30 yard dumpsters available!

one billboard is size 7x21 feet the other is 15x 21 ft

Target Market(s)

Contractors, home owners

Requirements
Must have
• Use font similar to logo that is eye catching

```html
<!DOCTYPE html>
<html lang="en">
<head>
<meta charset="utf-8">
<title>Boundless Haulbins Billboards</title>
<link rel="stylesheet" href="https://fonts.googleapis.com/css2?family=Saira:wght@700&family=Roboto+Condensed:wght@500;700&family=Anton&display=swap">
<style>
  :root {
    --page: #cfe0f2;
    --ink: #050608;
    --white: #ffffff;
    --purple: #7f3f98;
    --lilac-light: #b89cd2;
    --lilac-dark: #5a3b73;
    --photo-light: #3c3c3e;
    --photo-dark: #1c1c1e;
    --bin-green: #4cbf3e;
    --label: #0b0b0b;
  }
  * { margin: 0; padding: 0; box-sizing: border-box; }
  html, body { width: 840px; height: 1200px; overflow: hidden; }
  body { background: var(--page); position: relative; font-family: "Roboto Condensed", sans-serif; }
  .size-label {
    position: absolute;
    font-family: "Roboto Condensed", sans-serif;
    font-weight: 500;
    font-size: 40px;
    color: var(--label);
    transform: translateX(-50%);
  }
  .size-label--wide { left: 440px; top: 22px; }
  .size-label--tall { left: 350px; top: 1112px; }
  .billboard { position: absolute; display: block; }
  .billboard--wide { left: 45px; top: 98px; width: 717px; height: 238px; }
  .billboard--tall { left: 138px; top: 608px; width: 573px; height: 409px; }
  .brand { font-family: "Saira", sans-serif; font-weight: 700; fill: var(--white); }
  .tagline { font-family: "Roboto Condensed", sans-serif; font-weight: 700; fill: var(--white); }
  .phone { font-family: "Anton", sans-serif; fill: var(--white); }
  .web { font-family: "Roboto Condensed", sans-serif; font-weight: 700; fill: var(--white); }
</style>
</head>
<body>
  <div class="size-label size-label--wide">7x21</div>

  <svg class="billboard billboard--wide" viewBox="0 0 717 238" aria-label="7 by 21 foot billboard">
    <defs>
      <linearGradient id="wide-photo" x1="0" y1="0" x2="1" y2="1">
        <stop offset="0" stop-color="var(--lilac-light)"/>
        <stop offset="1" stop-color="var(--lilac-dark)"/>
      </linearGradient>
    </defs>
    <rect class="board-base" width="717" height="238" fill="var(--ink)"/>
    <polygon class="photo-area" role="img" aria-label="Photo of a pickup truck tipping a roll-off dumpster, tinted purple" points="330,0 717,0 717,238 436,238" fill="url(#wide-photo)"/>
    <polygon class="divider-stripe" points="318,0 330,0 436,238 424,238" fill="var(--white)"/>
    <polygon class="service-band" points="0,142 381,142 412,211 0,211" fill="var(--purple)"/>

    <text class="brand" x="40" y="84" font-size="46">BOUNDLESS</text>
    <text class="brand" x="318" y="116" font-size="24" text-anchor="end">HAULBINS</text>

    <text class="tagline" x="195" y="164" font-size="15" text-anchor="middle">RESIDENTIAL &amp; COMMERCIAL</text>
    <text class="tagline" x="200" y="199" font-size="32" text-anchor="middle">DUMPSTER RENTALS</text>

    <text class="tagline" x="666" y="20" font-size="11.5" text-anchor="middle" fill="var(--ink)" style="fill:var(--ink)">16/20/30 YARD</text>
    <text class="tagline" x="666" y="32" font-size="11.5" text-anchor="middle" style="fill:var(--ink)">DUMPSTERS</text>
    <text class="tagline" x="666" y="44" font-size="11.5" text-anchor="middle" style="fill:var(--ink)">AVAILABLE!</text>

    <rect class="bin-illustration" role="img" aria-label="Illustration of three green skip dumpsters in increasing sizes" x="449" y="82" width="234" height="64" rx="6" fill="var(--bin-green)"/>

    <text class="phone" x="569" y="188" font-size="44" text-anchor="middle">555-314-2087</text>
    <rect class="web-bar" x="435" y="195" width="282" height="24" fill="var(--ink)"/>
    <text class="web" x="569" y="213" font-size="17" text-anchor="middle">BOUNDLESSHAULBINS.COM</text>
  </svg>

  <svg class="billboard billboard--tall" viewBox="0 0 573 409" aria-label="15 by 21 foot billboard">
    <defs>
      <linearGradient id="tall-photo" x1="0" y1="0" x2="1" y2="1">
        <stop offset="0" stop-color="var(--photo-light)"/>
        <stop offset="1" stop-color="var(--photo-dark)"/>
      </linearGradient>
    </defs>
    <rect class="board-base" width="573" height="409" fill="var(--ink)"/>
    <rect class="photo-area" role="img" aria-label="Dark photo of a pickup truck tipping a roll-off dumpster" width="573" height="317" fill="url(#tall-photo)"/>

    <text class="brand" x="290" y="128" font-size="62" text-anchor="middle">BOUNDLESS</text>
    <text class="brand" x="447" y="163" font-size="34" text-anchor="end">HAULBINS</text>

    <rect class="bin-illustration" role="img" aria-label="Illustration of three green skip dumpsters in increasing sizes" x="29" y="214" width="314" height="89" rx="8" fill="var(--bin-green)"/>

    <text class="tagline" x="442" y="248" font-size="16" text-anchor="middle">16/20/30 YARD</text>
    <text class="tagline" x="442" y="268" font-size="16" text-anchor="middle">DUMPSTERS AVAILABLE!</text>

    <polygon class="service-band" points="0,327 296,327 318,380 0,380" fill="var(--purple)"/>
    <polygon class="contact-band" points="312,317 573,317 573,387 340,387" fill="var(--purple)"/>
    <polygon class="divider-stripe" points="298,317 310,317 338,387 326,387" fill="var(--white)"/>
    <rect class="web-bar" x="334" y="362" width="239" height="21" fill="var(--ink)"/>

    <text class="tagline" x="160" y="346" font-size="17" text-anchor="middle">RESIDENTIAL &amp; COMMERCIAL</text>
    <text class="tagline" x="160" y="375" font-size="26" text-anchor="middle">DUMPSTER RENTALS</text>

    <text class="phone" x="444" y="356" font-size="36" text-anchor="middle">555-314-2087</text>
    <text class="web" x="452" y="378" font-size="14" text-anchor="middle">BOUNDLESSHAULBINS.COM</text>
  </svg>

  <div class="size-label size-label--tall">15x21</div>
</body>
</html>
```